Fahrzeugbeschriftung für Brandschutzservice
Zielgruppe
Siehe bitte www.lorventa.de
Aufgabenstellung
Brandschutzservice / Kundendienst / Feuerlöscher vor Ort beim Kunden prüfen /

```html
<!DOCTYPE html>
<html lang="de">
<head>
<meta charset="utf-8">
<title>Fahrzeugbeschriftung Brandschutzservice</title>
<link href="https://fonts.googleapis.com/css2?family=Open+Sans:wght@400;600;700&display=swap" rel="stylesheet">
<style>
:root{
  --bg:#eceef0;
  --body:#ffffff;
  --edge:#c9cdd1;
  --orange:#e2620f;
  --orange-deep:#c94f06;
  --amber:#f2a516;
  --ink:#2a2a2a;
  --red:#d4241c;
  --white:#ffffff;
}
*{margin:0;padding:0;box-sizing:border-box}
html,body{width:1200px;height:2402px;overflow:hidden;background:var(--bg)}
body{font-family:"Open Sans",Arial,sans-serif;color:var(--ink);position:relative}
.view{position:absolute;left:0;width:1200px}
.view--left{top:0;height:800px}
.view--right{top:800px;height:800px}
.view--rear{top:1600px;height:802px}
.panel{position:absolute}
.brand{position:absolute;display:flex;align-items:flex-start;gap:12px}
.brand__dot{width:34px;height:34px;border-radius:50%;background:var(--red);flex:none;margin-top:4px}
.brand__name{font-weight:700;font-size:17px;line-height:1.2;color:var(--ink)}
.brand__lines{font-weight:400;font-size:13px;line-height:1.3;color:var(--ink)}
.slogan{position:absolute;font-weight:700;font-size:27px;line-height:1.2;color:var(--ink);letter-spacing:.3px}
.contact{position:absolute;font-size:13px;line-height:1.35;color:var(--ink)}
.contact__title{font-weight:700;font-size:15px;line-height:1.25}
.contact__phone{font-weight:700;font-size:19px;margin-top:4px}
.contact__small{font-size:10px}
.web{position:absolute;font-weight:700;font-size:22px;color:var(--white)}
.rear-slogan{position:absolute;font-weight:400;font-size:36px;line-height:1.2;color:var(--ink)}
.rear-phone{position:absolute;left:0;width:1200px;text-align:center;font-weight:700;font-size:36px;color:var(--white)}
</style>
</head>
<body>

<section class="view view--left">
  <svg class="panel" style="left:90px;top:290px" width="1020" height="370" viewBox="0 0 1020 370">
    <defs>
      <linearGradient id="flameL" x1="0" y1="0" x2="1" y2="1">
        <stop offset="0" stop-color="var(--orange-deep)"/>
        <stop offset="1" stop-color="var(--orange)"/>
      </linearGradient>
    </defs>
    <rect x="0" y="0" width="1020" height="370" rx="28" fill="var(--body)" stroke="var(--edge)" stroke-width="2"/>
    <path role="img" aria-label="Flammenmotiv in Orange und Gelb" d="M2 40 Q2 2 40 2 H190 C280 60 330 170 450 230 C520 265 560 320 600 368 H2 Z" fill="url(#flameL)"/>
    <path d="M190 2 C280 60 330 170 450 230 C520 265 560 320 600 368" fill="none" stroke="var(--amber)" stroke-width="10"/>
    <line x1="540" y1="10" x2="540" y2="360" stroke="var(--edge)" stroke-width="2"/>
  </svg>
  <div class="brand" style="left:375px;top:330px">
    <span class="brand__dot"></span>
    <div><div class="brand__name">Saalwinkeler<br>Brandschutzservice</div>
    <div class="brand__lines">Feuerlöschtechnik<br>Löschanlagen<br>Service &amp; Zubehör</div></div>
  </div>
  <div class="slogan" style="left:275px;top:475px">BERATUNG<br>&nbsp;&nbsp;&nbsp;VERKAUF<br>&nbsp;&nbsp;&nbsp;&nbsp;&nbsp;&nbsp;SERVICE</div>
  <div class="contact" style="left:665px;top:478px">
    <div class="contact__title">SAALWINKELER<br>BRANDSCHUTZSERVICE</div>
    <div>Inh. Jonas Hermel</div>
    <div>Lindenweg 12 | 07700 Musterau</div>
    <div class="contact__phone">Tel. : 03000 / 47 19 52</div>
    <div class="contact__small">Fax. : 03000 / 47 19 53<br>Funk. : 0170 / 000 4812</div>
  </div>
  <div class="web" style="left:400px;top:608px">www.lorventa.de</div>
</section>

<section class="view view--right">
  <svg class="panel" style="left:90px;top:290px" width="1020" height="370" viewBox="0 0 1020 370">
    <defs>
      <linearGradient id="flameR" x1="1" y1="0" x2="0" y2="1">
        <stop offset="0" stop-color="var(--orange-deep)"/>
        <stop offset="1" stop-color="var(--orange)"/>
      </linearGradient>
    </defs>
    <rect x="0" y="0" width="1020" height="370" rx="28" fill="var(--body)" stroke="var(--edge)" stroke-width="2"/>
    <path role="img" aria-label="Flammenmotiv in Orange und Gelb" d="M1018 40 Q1018 2 980 2 H840 C760 80 680 150 590 200 C520 240 470 300 430 368 H1018 Z" fill="url(#flameR)"/>
    <path d="M840 2 C760 80 680 150 590 200 C520 240 470 300 430 368" fill="none" stroke="var(--amber)" stroke-width="10"/>
    <line x1="470" y1="10" x2="470" y2="360" stroke="var(--edge)" stroke-width="2"/>
  </svg>
  <div class="brand" style="left:580px;top:325px">
    <span class="brand__dot"></span>
    <div><div class="brand__name">Saalwinkeler<br>Brandschutzservice</div>
    <div class="brand__lines">Feuerlöschtechnik<br>Löschanlagen<br>Service &amp; Zubehör</div></div>
  </div>
  <div class="slogan" style="left:700px;top:475px">&nbsp;&nbsp;&nbsp;&nbsp;&nbsp;&nbsp;BERATUNG<br>&nbsp;&nbsp;&nbsp;VERKAUF<br>SERVICE</div>
  <div class="contact" style="left:360px;top:485px">
    <div class="contact__title">SAALWINKELER<br>BRANDSCHUTZSERVICE</div>
    <div>Inh. Jonas Hermel</div>
    <div>Lindenweg 12 | 07700 Musterau</div>
    <div class="contact__phone">Tel. : 03000 / 47 19 52</div>
    <div class="contact__small">Fax. : 03000 / 47 19 53<br>Funk. : 0170 / 000 4812</div>
  </div>
  <div class="web" style="left:590px;top:605px">www.lorventa.de</div>
</section>

<section class="view view--rear">
  <svg class="panel" style="left:280px;top:90px" width="640" height="560" viewBox="0 0 640 560">
    <defs>
      <linearGradient id="rearFill" x1="0" y1="0" x2="0" y2="1">
        <stop offset="0" stop-color="var(--orange)"/>
        <stop offset="1" stop-color="var(--orange-deep)"/>
      </linearGradient>
    </defs>
    <path d="M30 0 H610 Q640 0 640 30 V560 H0 V30 Q0 0 30 0 Z" fill="url(#rearFill)"/>
    <path role="img" aria-label="Flammenmotiv am Heck" d="M60 10 H580 L610 200 C560 200 520 210 480 240 L500 210 H140 L160 240 C120 210 80 200 30 200 Z" fill="var(--body)"/>
    <path d="M30 200 C80 200 120 210 160 240 M610 200 C560 200 520 210 480 240" fill="none" stroke="var(--amber)" stroke-width="8"/>
    <line x1="320" y1="10" x2="320" y2="560" stroke="var(--orange-deep)" stroke-width="2" opacity=".6"/>
  </svg>
  <div class="brand" style="left:360px;top:170px">
    <span class="brand__dot"></span>
    <div><div class="brand__name">Saalwinkeler<br>Brandschutzservice</div>
    <div class="brand__lines">Feuerlöschtechnik<br>Löschanlagen<br>Service &amp; Zubehör</div></div>
  </div>
  <div class="rear-slogan" style="left:615px;top:145px">BERATUNG<br>VERKAUF<br>SERVICE</div>
  <div class="rear-phone" style="top:525px">Tel. : 03000 / 47 19 52</div>
</section>

</body>
</html>
```